Namecard design for Forex trading & training company

We need a design for a financial forex trading company.
Namecard should give customer a professional yet premium feel, able to differentiate from others.
1) most financial companies employs white background, while its clean and professional, it is too mainstream.
2) I am thinking of brown as base colour, however it easily gives the perception of being an Interior Design company
3) Task is to find a design that is able to portray a clean professional feel, at the same time, appear premium and differentiated from others.
*I'll be employing 3D textured print for my company namecard just so as to give it a better finishing.
Please find attached for my logo.
Financial

```html
<!DOCTYPE html>
<html lang="en">
<head>
<meta charset="utf-8">
<title>Valtren Capital – Business Card</title>
<link rel="stylesheet" href="https://fonts.googleapis.com/css2?family=Cormorant+Garamond:wght@500;600&family=Open+Sans:wght@400;600&display=swap">
<style>
  :root {
    --backdrop: #6b5236;
    --card-dark: #111111;
    --card-light: #ffffff;
    --ink-light: #ffffff;
    --ink-muted: #d8d8d8;
    --ink-dark: #1c1c1c;
    --brand-navy: #2e2a86;
    --card-edge: #2a2a2a;
  }
  * { margin: 0; padding: 0; box-sizing: border-box; }
  html, body {
    width: 1200px;
    height: 1000px;
    overflow: hidden;
  }
  body {
    background: var(--backdrop);
    position: relative;
    font-family: "Open Sans", sans-serif;
  }
  .card {
    position: absolute;
    width: 614px;
    height: 360px;
    border-radius: 14px;
  }
  .card--front {
    left: 292px;
    top: 126px;
    background: var(--card-dark);
    color: var(--ink-light);
  }
  .card--back {
    left: 293px;
    top: 514px;
    background: var(--card-light);
    border: 1px solid var(--card-edge);
    color: var(--ink-dark);
  }
  .brand-mark {
    position: absolute;
    display: flex;
    align-items: center;
    gap: 14px;
    font-family: "Cormorant Garamond", serif;
    font-weight: 600;
    font-size: 44px;
    letter-spacing: 2px;
  }
  .brand-mark__square {
    width: 26px;
    height: 26px;
  }
  .card--front .brand-mark {
    left: 0;
    right: 0;
    top: 130px;
    justify-content: center;
  }
  .card--front .brand-mark__square { background: var(--ink-light); }
  .card--back .brand-mark {
    right: 34px;
    top: 74px;
    color: var(--brand-navy);
  }
  .card--back .brand-mark__square { background: var(--brand-navy); }
  .wordmark {
    position: absolute;
    font-family: "Cormorant Garamond", serif;
    font-weight: 500;
    font-size: 15px;
    letter-spacing: 4.6px;
    text-transform: uppercase;
    white-space: nowrap;
  }
  .card--front .wordmark {
    left: 0;
    right: 0;
    top: 256px;
    text-align: center;
  }
  .card--back .wordmark {
    right: 30px;
    top: 168px;
    color: var(--brand-navy);
  }
  .website {
    position: absolute;
    left: 0;
    right: 0;
    top: 316px;
    text-align: center;
    font-size: 15px;
    color: var(--ink-muted);
  }
  .contact {
    position: absolute;
    right: 34px;
    text-align: right;
    font-size: 14px;
    line-height: 20px;
  }
  .contact--person { top: 218px; }
  .contact__name {
    font-weight: 600;
    font-size: 16px;
    line-height: 24px;
  }
  .contact--reach { top: 290px; }
</style>
</head>
<body>
  <section class="card card--front">
    <div class="brand-mark"><span class="brand-mark__square"></span>Valtren</div>
    <p class="wordmark">Valtren Capital</p>
    <p class="website">www.valtrencap.com</p>
  </section>

  <section class="card card--back">
    <div class="brand-mark"><span class="brand-mark__square"></span>Valtren</div>
    <p class="wordmark">Valtren Capital</p>
    <div class="contact contact--person">
      <p class="contact__name">Marcus Lien</p>
      <p class="contact__role">Pantry Manager</p>
    </div>
    <div class="contact contact--reach">
      <p>(86) 555 010 234</p>
      <p>marcus@valtrencap.com</p>
    </div>
  </section>
</body>
</html>
```